Designer and consultant for professionals/businesses and manufacturers in the kitchen and bath in...

I have 30 years of design experience, and 19 of those years within the marketing team of a national cabinet manufacturer. This role gave me the opportunity to consult and design for kitchen/bath businesses, from boutique to multi-store national scale. My services include layout and spatial planning, individual display design, and product design for cabinet manufacturers. From showrooms, to trade shows to integrated design collections. I would like to see designs that convey professionalism, as well as an appeal to the creative designer mind!

Target Market(s)

Kitchen and bath dealers, as well as mid-scale multi-store home centers. Cabinet manufacturers, Trade Show agencies.

Industry/Entity Type

Kitchen

Contact Information for Business Card

Serving Kitchen and Bath Businesses

Logo Text

MT (initials for business name)

Font styles to use
Serif
Sans Serif
Decorative

Colors
e34197

Requirements
Must have
• Marlowe Tavish Design and Consulting, Inc. (business name)
• marlowe@mtvantra.com (email)
• 917-555-0148 (phone)
• mtvantra.com (website)
Nice to have
• Inclusions of geometric shapes; particularly a 30/15 degree triangle and circle(s)
• 2 colors
Should not have
• Not too artsy!

```html
<!DOCTYPE html>
<html lang="en">
<head>
<meta charset="utf-8">
<title>Marlowe Tavish Design and Consulting, Inc. — Business Card</title>
<link rel="stylesheet" href="https://fonts.googleapis.com/css2?family=Cinzel:wght@400;500&family=Montserrat:ital,wght@0,400;0,500;1,700&display=swap">
<style>
  :root {
    --backdrop: #c9c9c9;
    --card-pink: #f4bfca;
    --card-white: #ffffff;
    --ink-dark: #3a3a3a;
    --ink-grey: #8a8a8a;
    --accent-pink: #f0a9b8;
    --mark-dark: #4a4a4a;
  }
  * { margin: 0; padding: 0; box-sizing: border-box; }
  html, body { width: 1200px; height: 800px; overflow: hidden; }
  body {
    position: relative;
    background: var(--backdrop);
    font-family: "Montserrat", sans-serif;
  }
  .card {
    position: absolute;
    top: 257px;
    width: 500px;
    height: 286px;
    border-radius: 18px;
    box-shadow: 0 14px 30px rgba(0,0,0,0.18);
  }
  .card--front { left: 70px; background: var(--card-pink); }
  .card--back { left: 630px; background: var(--card-white); }

  /* Front */
  .front-lockup {
    position: absolute;
    left: 50%; top: 50%;
    transform: translate(-50%, -50%);
    display: flex;
    align-items: center;
    gap: 18px;
  }
  .mark-circle {
    width: 86px; height: 86px;
    border-radius: 50%;
    background: var(--mark-dark);
    flex-shrink: 0;
  }
  .wordmark {
    font-family: "Cinzel", serif;
    font-weight: 500;
    font-size: 24px;
    letter-spacing: 1.5px;
    line-height: 1;
  }
  .card--front .wordmark { color: var(--ink-dark); }
  .tagline {
    margin-top: 6px;
    font-family: "Montserrat", sans-serif;
    font-size: 9.5px;
    letter-spacing: 2.4px;
    text-transform: uppercase;
  }
  .card--front .tagline { color: var(--ink-dark); }

  /* Back */
  .back-mark {
    position: absolute;
    right: 34px; top: 30px;
    width: 90px; height: 90px;
    border-radius: 50%;
    background: var(--mark-dark);
  }
  .back-heading {
    position: absolute;
    left: 36px; top: 112px;
  }
  .card--back .wordmark { color: var(--ink-grey); font-size: 23px; }
  .card--back .tagline { color: var(--ink-grey); }
  .contact-person {
    position: absolute;
    left: 36px; top: 170px;
  }
  .person-name {
    font-family: "Cinzel", serif;
    font-size: 15px;
    letter-spacing: 1px;
    color: var(--accent-pink);
  }
  .person-title {
    font-size: 10px;
    color: var(--ink-grey);
    margin-top: 2px;
  }
  .contact-list {
    position: absolute;
    left: 36px; top: 222px;
    list-style: none;
    font-size: 10.5px;
    line-height: 1.5;
    color: var(--ink-grey);
  }
  .contact-label {
    font-weight: 700;
    font-style: italic;
    color: var(--ink-grey);
  }
</style>
</head>
<body>
  <section class="card card--front" aria-label="Business card front">
    <div class="front-lockup">
      <div class="mark-circle" aria-hidden="true"></div>
      <div class="brand">
        <div class="wordmark">MARLOWE TAVISH</div>
        <div class="tagline">Design and Consulting, Inc.</div>
      </div>
    </div>
  </section>

  <section class="card card--back" aria-label="Business card back">
    <div class="back-mark" aria-hidden="true"></div>
    <div class="back-heading">
      <div class="wordmark">MARLOWE TAVISH</div>
      <div class="tagline">Design and Consulting, Inc.</div>
    </div>
    <div class="contact-person">
      <div class="person-name">MARLOWE TAVISH</div>
      <div class="person-title">Managing Director</div>
    </div>
    <ul class="contact-list">
      <li><span class="contact-label">email:</span> marlowe@mtvantra.com</li>
      <li><span class="contact-label">phone:</span> 917-555-0148</li>
      <li><span class="contact-label">web:</span> mtvantra.com</li>
    </ul>
  </section>
</body>
</html>
```